The company Velquist needs a design for CBD capsules

We (Velquist) need a new design for our CBD capsules. We already have a design for CBD oil. However, we do not want to use this completely. The Talmbex label and the cans serve as a template. Please upload in the format 139mm x 59mm incl.
2mm bleed all around and in .pdf vector. The logo files for Velquist are included in the briefing.

Industry/Entity Type

Onlineshop

Colors
00AB8E
00BBA5
67D7C9
C6EFE9
E9F9F6

Requirements
Must have
• Please in the format 139mm x 59mm incl. 2mm bleed all around and .pdf vector
Should not have
• It shouldn't be the same label, but it should be recognizable.

```html
<!DOCTYPE html>
<html lang="de">
<head>
<meta charset="utf-8">
<title>Velquist CBD Kapseln – Etikett 139 × 59 mm</title>
<link rel="stylesheet" href="https://fonts.googleapis.com/css2?family=Playfair+Display:wght@800;900&family=Josefin+Sans:wght@600&family=Sacramento&display=swap">
<style>
  :root{
    --stage:#5a5a5a;
    --mint-50:#E9F9F6;
    --mint-100:#C6EFE9;
    --mint-300:#67D7C9;
    --teal-500:#00BBA5;
    --teal-600:#00AB8E;
    --band-dark:#14917c;
    --frame:#3fb6a6;
    --ink:#1f4b57;
    --leaf-green:#9dbf4a;
    --white:#ffffff;
  }
  html,body{margin:0;padding:0;width:1152px;height:1200px;overflow:hidden;background:var(--stage);}
  .canvas{position:relative;width:1152px;height:1200px;}
  .label{position:absolute;left:26px;top:366px;width:1100px;height:467px;overflow:hidden;background:var(--mint-50);}
  .label__pattern{position:absolute;left:0;top:0;width:1100px;height:360px;
    background:radial-gradient(ellipse at 50% 45%, #eefbf8 0%, var(--mint-50) 50%, #dcf3ee 100%);}
  .label__frame{position:absolute;left:0;top:0;width:1100px;height:360px;}
  .label__text{position:absolute;left:330px;width:440px;text-align:center;margin:0;line-height:1;}
  .brand{top:72px;font-family:"Playfair Display",serif;font-weight:800;font-size:46px;color:var(--ink);letter-spacing:-0.5px;}
  .product{top:128px;font-family:"Playfair Display",serif;font-weight:900;font-size:96px;color:var(--leaf-green);}
  .form{top:226px;font-family:"Playfair Display",serif;font-weight:900;font-size:37px;color:var(--ink);letter-spacing:0.5px;}
  .divider{position:absolute;left:505px;top:272px;width:90px;height:3px;background:var(--frame);}
  .claim{font-family:"Josefin Sans",sans-serif;font-weight:600;font-size:19px;color:var(--ink);letter-spacing:1.5px;}
  .claim--vegan{top:286px;}
  .claim--gmo{top:314px;}
  .band{position:absolute;left:0;top:360px;width:1100px;height:107px;
    background:linear-gradient(90deg,var(--teal-600) 0%,var(--band-dark) 45%,var(--teal-500) 100%);}
  .band__script{position:absolute;left:320px;top:368px;width:410px;text-align:center;margin:0;
    font-family:"Sacramento",cursive;font-size:76px;line-height:1;color:var(--white);}
  .strength-badge{position:absolute;left:748px;top:318px;width:80px;height:80px;border-radius:50%;
    background:var(--white);border:3px solid var(--teal-600);display:flex;align-items:center;justify-content:center;
    font-family:"Josefin Sans",sans-serif;font-weight:600;font-size:24px;color:var(--band-dark);}
</style>
</head>
<body>
<div class="canvas">
  <div class="label">
    <div class="label__pattern" role="img" aria-label="Faint pattern of hemp leaves and dots in pale mint tones"></div>
    <svg class="label__frame" viewBox="0 0 1100 360" aria-hidden="true">
      <path d="M290 338 Q330 338 330 300 L330 76 Q330 46 360 46 L740 46 Q770 46 770 76 L770 300 Q770 338 810 338"
            fill="none" stroke="var(--frame)" stroke-width="2.5"/>
    </svg>
    <p class="label__text brand">Velquist</p>
    <p class="label__text product">CBD</p>
    <p class="label__text form">KAPSELN</p>
    <div class="divider"></div>
    <p class="label__text claim claim--vegan">VEGAN</p>
    <p class="label__text claim claim--gmo">GENTECHIK FREI</p>
    <div class="band"></div>
    <p class="band__script">full spectrum</p>
    <div class="strength-badge">10%</div>
  </div>
</div>
</body>
</html>
```